I am a company selling interior designing materials

HI, I am selling interior design materials and require a namecard which is more outstanding while following a certain details placement as attached.

My clients are mainly interior designers so it has to attract their attention rather than feeling that its "just another namecard". I am selling wallcoverings, fabrics, acoustics and carpets.

Target Market(s)

interior designers designing hotels, commerical offices.

Contact Information for Business Card

As per attached.
Please change address to 47 Jalan 16 Tampines #05-02 Velmora Building Singapore 527314

Font styles to use
Other font styles liked:
• calibri

Requirements
Must have
• (1) company logo on top in the middle. Placement of contac details to be the same
• (2) company color is blue/green cymk 75/8/42/0
• (3) "KTV" logo to be prominent
• (4) You may change the logo but there should be a "swirl" surrounding the word KTV like current logo. The swirl pattern does not need to follow current logo and you may propose.
Should not have
• (1) there should not be any designs above "KTV" logo
• (2) no sharp triangles or angles

```html
<!DOCTYPE html>
<html lang="en">
<head>
<meta charset="utf-8">
<title>KTV Business Card</title>
<link rel="stylesheet" href="https://fonts.googleapis.com/css2?family=Open+Sans:wght@400;600;700&display=swap">
<style>
  :root {
    --teal: #2fb3a0;
    --teal-light: #9fd8cd;
    --band-white: #ffffff;
    --slate-dark: #3d3e40;
    --slate-mid: #58595b;
    --slate-light: #6a6b6d;
    --text: #ffffff;
    --page: #ffffff;
  }
  * { margin: 0; padding: 0; box-sizing: border-box; }
  html, body {
    width: 945px;
    height: 1200px;
    overflow: hidden;
    background: var(--page);
    font-family: "Open Sans", Calibri, sans-serif;
    color: var(--text);
  }
  .canvas { position: relative; width: 945px; height: 1200px; }

  .card {
    position: absolute;
    left: 3px;
    width: 940px;
    height: 533px;
  }
  .card--front { top: 0; }
  .card--back { top: 667px; }

  .card__band {
    position: absolute;
    left: 0;
    width: 100%;
    height: 45px;
    background: linear-gradient(90deg, var(--teal) 0%, var(--teal-light) 30%, var(--band-white) 50%, var(--teal-light) 70%, var(--teal) 100%);
  }
  .card__band--top { top: 0; }
  .card__band--bottom { bottom: 0; }

  .card__field {
    position: absolute;
    left: 0;
    top: 45px;
    width: 100%;
    height: 443px;
    background:
      radial-gradient(ellipse at 50% 25%, var(--slate-light) 0%, var(--slate-mid) 45%, transparent 80%),
      linear-gradient(135deg, var(--slate-dark) 0%, var(--slate-mid) 50%, var(--slate-dark) 100%);
  }

  .wordmark {
    position: absolute;
    left: 0;
    width: 100%;
    text-align: center;
    font-weight: 700;
    line-height: 1;
    letter-spacing: 2px;
  }
  .card--front .wordmark { top: 108px; font-size: 62px; }
  .card--back .wordmark { top: 170px; font-size: 120px; letter-spacing: 4px; }

  .company-name {
    position: absolute;
    top: 213px;
    width: 100%;
    text-align: center;
    font-size: 16.5px;
  }
  .person-name {
    position: absolute;
    top: 268px;
    width: 100%;
    text-align: center;
    font-size: 39px;
    font-weight: 700;
  }
  .person-phone {
    position: absolute;
    top: 322px;
    width: 100%;
    text-align: center;
    font-size: 25px;
  }

  .contact {
    position: absolute;
    top: 405px;
    font-size: 25px;
    line-height: 32px;
  }
  .contact--address { left: 21px; width: 420px; }
  .contact--office { right: 21px; text-align: right; }

  .offerings {
    position: absolute;
    top: 370px;
    left: 0;
    width: 100%;
    list-style: none;
    font-size: 32px;
  }
  .offerings li { position: absolute; top: 0; white-space: nowrap; }
  .offerings li:nth-child(1) { left: 122px; }
  .offerings li:nth-child(2) { left: 383px; }
  .offerings li:nth-child(3) { left: 561px; }
  .offerings li:nth-child(4) { left: 716px; }
</style>
</head>
<body>
<main class="canvas">

  <section class="card card--front">
    <div class="card__band card__band--top"></div>
    <div class="card__field" role="img" aria-label="Soft grey faceted background texture"></div>
    <div class="card__band card__band--bottom"></div>

    <div class="wordmark">KTV</div>
    <p class="company-name">KaiTeva Interior Furnishings Pte Ltd</p>
    <h1 class="person-name">Serene Lim</h1>
    <p class="person-phone">(65) 9172 4605</p>

    <address class="contact contact--address">47 Jalan 16 Tampines #05-02 Velmora Building Singapore 527314</address>
    <address class="contact contact--office">(65) 6283 7140<br>serene@ktvfurnishings.com</address>
  </section>

  <section class="card card--back">
    <div class="card__band card__band--top"></div>
    <div class="card__field" role="img" aria-label="Soft grey faceted background texture"></div>
    <div class="card__band card__band--bottom"></div>

    <div class="wordmark">KTV</div>
    <ul class="offerings">
      <li>Wallcoverings</li>
      <li>Acoustic</li>
      <li>Fabrics</li>
      <li>Carpet</li>
    </ul>
  </section>

</main>
</body>
</html>
```